Infographic for B2B Service solution offering (sales funnel)

Attached is an example of something we need assistance with making into a more professional infographic. These infographics are for our B2B marketing services, aimed at IT Consulting firms.

We have done some basic graphics (attached) and this will provide you guidance (video link on google sheet):
https://pages.vardolink.net/sheet/r/7kQm3TzP9wLcYe2HbNvAsDxR4uFgJ8tWoZiE6yKpBq/view?mode=shared

Here are some examples you can model for the new infographic:
https://vault.vardolink.net/store/groups/48PkTwMz3nRq9LbXvYc-hsd2FjQe?ref=store_link

Target Market(s)

B2B IT Consulting Firms

Industry/Entity Type

Information Technology, Consulting

Colors

Designer to choose colors to be used in the design.

Requirements
Must have
• professional, high level consulting firms are target market
Should not have
• cartoonish

```html
<!DOCTYPE html>
<html lang="en">
<head>
<meta charset="utf-8">
<title>Creating B2B Relationships: The Grow It</title>
<link rel="stylesheet" href="https://fonts.googleapis.com/css2?family=Barlow+Condensed:wght@700;800&display=swap">
<style>
  :root {
    --ink-navy: #0b3566;
    --ink-white: #ffffff;
    --ink-black: #0a0a0a;
    --stage-gray: #d9dbdf;
    --stage-glow: #fff4e2;
    --paper: #ffffff;
    --blue-deep: #0a86cf;
    --blue-mid: #19aeea;
    --blue-bright: #2cc4f5;
    --cyan-pale: #d6f7fd;
    --cyan-soft: #9fe3f6;
    --cyan-edge: #6fcdea;
    --meter-green: #1fd23a;
    --meter-yellow: #f4ee2a;
    --meter-orange: #f39a2a;
    --meter-red: #f24545;
  }
  * { margin: 0; padding: 0; box-sizing: border-box; }
  html, body { width: 1200px; height: 957px; overflow: hidden; background: var(--paper); }
  .infographic { display: block; width: 1200px; height: 957px; }
  .funnel-text { font-family: "Barlow Condensed", "Arial Narrow", sans-serif; font-weight: 800; }
  .offer-text { font-family: "Barlow Condensed", "Arial Narrow", sans-serif; font-weight: 700; font-size: 32px; }
  .note-text { font-family: "Barlow Condensed", "Arial Narrow", sans-serif; font-weight: 800; font-size: 46px; fill: var(--ink-black); }
  .on-deep { fill: var(--ink-white); }
  .on-pale { fill: var(--ink-navy); }
</style>
</head>
<body>
<svg class="infographic" viewBox="0 0 1350 1080" preserveAspectRatio="none" xmlns="http://www.w3.org/2000/svg">
  <defs>
    <radialGradient id="stageGlow" cx="330" cy="300" r="700" gradientUnits="userSpaceOnUse">
      <stop offset="0" stop-color="var(--stage-glow)"/>
      <stop offset="0.55" stop-color="#e4e4e6"/>
      <stop offset="1" stop-color="var(--stage-gray)"/>
    </radialGradient>
    <linearGradient id="deepBody" x1="0" y1="0" x2="1" y2="0">
      <stop offset="0" stop-color="var(--blue-deep)"/>
      <stop offset="0.45" stop-color="var(--blue-bright)"/>
      <stop offset="1" stop-color="var(--blue-deep)"/>
    </linearGradient>
    <linearGradient id="deepTop" x1="0" y1="0" x2="0" y2="1">
      <stop offset="0" stop-color="#5fd8fb"/>
      <stop offset="1" stop-color="var(--blue-mid)"/>
    </linearGradient>
    <linearGradient id="paleBody" x1="0" y1="0" x2="1" y2="0">
      <stop offset="0" stop-color="var(--cyan-edge)"/>
      <stop offset="0.45" stop-color="var(--cyan-pale)"/>
      <stop offset="1" stop-color="var(--cyan-edge)"/>
    </linearGradient>
    <linearGradient id="paleTop" x1="0" y1="0" x2="0" y2="1">
      <stop offset="0" stop-color="#f2fdff"/>
      <stop offset="1" stop-color="var(--cyan-soft)"/>
    </linearGradient>
    <linearGradient id="deepBand" x1="0" y1="0" x2="0" y2="1">
      <stop offset="0" stop-color="var(--blue-mid)"/>
      <stop offset="1" stop-color="var(--blue-deep)"/>
    </linearGradient>
    <linearGradient id="paleBand" x1="0" y1="0" x2="0" y2="1">
      <stop offset="0" stop-color="#e9fcff"/>
      <stop offset="1" stop-color="var(--cyan-soft)"/>
    </linearGradient>
    <linearGradient id="meter" x1="0" y1="288" x2="0" y2="1050" gradientUnits="userSpaceOnUse">
      <stop offset="0" stop-color="var(--meter-green)"/>
      <stop offset="0.2" stop-color="var(--meter-green)"/>
      <stop offset="0.3" stop-color="var(--meter-yellow)"/>
      <stop offset="0.45" stop-color="var(--meter-yellow)"/>
      <stop offset="0.52" stop-color="var(--meter-orange)"/>
      <stop offset="0.58" stop-color="var(--meter-red)"/>
      <stop offset="1" stop-color="var(--meter-red)"/>
    </linearGradient>
    <path id="titleArc" d="M212,122 Q545,12 878,122"/>
  </defs>

  <!-- stage -->
  <rect class="stage" x="0" y="0" width="1082" height="1080" fill="url(#stageGlow)"/>

  <!-- risk meter -->
  <g class="risk-meter" fill="url(#meter)">
    <rect x="95" y="288" width="18" height="32"/>
    <rect x="95" y="334" width="18" height="32"/>
    <rect x="95" y="380" width="18" height="32"/>
    <rect x="95" y="426" width="18" height="32"/>
    <rect x="95" y="472" width="18" height="32"/>
    <rect x="95" y="518" width="18" height="32"/>
    <rect x="95" y="564" width="18" height="32"/>
    <rect x="95" y="610" width="18" height="32"/>
    <rect x="95" y="656" width="18" height="32"/>
    <rect x="95" y="702" width="18" height="32"/>
    <rect x="95" y="748" width="18" height="32"/>
    <rect x="95" y="794" width="18" height="32"/>
    <rect x="95" y="840" width="18" height="32"/>
    <rect x="95" y="886" width="18" height="32"/>
    <rect x="95" y="932" width="18" height="32"/>
    <rect x="95" y="978" width="18" height="28"/>
    <path d="M76,1012 L104,1040 L132,1012" fill="none" stroke="var(--meter-red)" stroke-width="9" stroke-linecap="round" stroke-linejoin="round"/>
  </g>

  <!-- title funnel -->
  <g class="title-funnel">
    <path d="M190,75 L230,215 A318,45 0 0 0 866,215 L898,75 Z" fill="url(#deepBody)"/>
    <ellipse cx="544" cy="75" rx="354" ry="55" fill="url(#deepTop)"/>
    <ellipse cx="548" cy="215" rx="300" ry="34" fill="#0c93d6" opacity="0.55"/>
    <text class="funnel-text on-deep" font-size="46" text-anchor="middle"><textPath href="#titleArc" startOffset="50%">CREATING B2B RELATIONSHIPS:</textPath></text>
    <text class="funnel-text on-deep" x="546" y="140" font-size="46" text-anchor="middle">THE GROW IT</text>
  </g>

  <!-- offer bands -->
  <g class="offer-bands">
    <rect x="390" y="288" width="585" height="100" fill="url(#deepBand)"/>
    <rect x="390" y="400" width="585" height="98" fill="url(#paleBand)"/>
    <rect x="390" y="512" width="585" height="98" fill="url(#deepBand)"/>
    <rect x="390" y="625" width="585" height="97" fill="url(#paleBand)"/>
    <rect x="390" y="737" width="585" height="98" fill="url(#deepBand)"/>
    <rect x="390" y="850" width="585" height="95" fill="url(#paleBand)"/>
    <rect x="390" y="962" width="585" height="93" fill="url(#deepBand)"/>
  </g>

  <g class="offer-text" text-anchor="end">
    <text class="on-deep" x="960" y="334">OFFER #1 - LOW RISK,</text>
    <text class="on-deep" x="960" y="370">LOW INVESTMENT</text>
    <text class="on-pale" x="960" y="443">OFFER #2 - LOW RISK,</text>
    <text class="on-pale" x="960" y="480">MEDIUM INVESTMENT</text>
    <text class="on-deep" x="960" y="556">OFFER #3 - MEDIUM RISK,</text>
    <text class="on-deep" x="960" y="593">MEDIUM INVESTMENT</text>
    <text class="on-pale" x="960" y="668">OFFER #4 - HIGH RISK,</text>
    <text class="on-pale" x="960" y="705">MEDIUM INVESTMENT</text>
    <text class="on-deep" x="960" y="780">OFFER #5 - MEDIUM RISK,</text>
    <text class="on-deep" x="960" y="817">HIGH INVESTMENT</text>
    <text class="on-pale" x="960" y="892">OFFER #6 - HIGH RISK,</text>
    <text class="on-pale" x="960" y="929">HIGH INVESTMENT</text>
    <text class="on-deep" x="960" y="997">OFFER #7 - HIGH RISK,</text>
    <text class="on-deep" x="960" y="1034">HIGH INVESTMENT</text>
  </g>

  <!-- funnel tiers -->
  <g class="funnel-tiers">
    <g class="tier tier-phone">
      <path d="M165,318 L185,395 A203,25 0 0 0 590,395 L610,318 Z" fill="url(#deepBody)"/>
      <ellipse cx="387" cy="318" rx="222" ry="28" fill="url(#deepTop)"/>
      <text class="funnel-text on-deep" x="388" y="403" font-size="44" text-anchor="middle">PHONE #</text>
    </g>
    <g class="tier tier-coffee">
      <path d="M195,425 L210,505 A178,22 0 0 0 565,505 L580,425 Z" fill="url(#paleBody)"/>
      <ellipse cx="387" cy="425" rx="193" ry="25" fill="url(#paleTop)"/>
      <text class="funnel-text on-pale" x="390" y="502" font-size="44" text-anchor="middle">COFFEE</text>
    </g>
    <g class="tier tier-dinner">
      <path d="M218,535 L232,610 A154,20 0 0 0 540,610 L555,535 Z" fill="url(#deepBody)"/>
      <ellipse cx="386" cy="535" rx="169" ry="23" fill="url(#deepTop)"/>
      <text class="funnel-text on-deep" x="388" y="609" font-size="44" text-anchor="middle">DINNER</text>
    </g>
    <g class="tier tier-weekend">
      <path d="M243,645 L255,718 A132,18 0 0 0 518,718 L530,645 Z" fill="url(#paleBody)"/>
      <ellipse cx="386" cy="645" rx="144" ry="21" fill="url(#paleTop)"/>
      <text class="funnel-text on-pale" x="388" y="700" font-size="34" text-anchor="middle">WEEKEND TRAVEL</text>
    </g>
    <g class="tier tier-parents">
      <path d="M268,757 L280,828 A107,16 0 0 0 493,828 L505,757 Z" fill="url(#deepBody)"/>
      <ellipse cx="386" cy="757" rx="119" ry="19" fill="url(#deepTop)"/>
      <text class="funnel-text on-deep" x="388" y="812" font-size="31" text-anchor="middle">MEET PARENTS</text>
    </g>
    <g class="tier tier-move-in">
      <path d="M293,868 L303,940 A85,14 0 0 0 472,940 L482,868 Z" fill="url(#paleBody)"/>
      <ellipse cx="387" cy="868" rx="95" ry="17" fill="url(#paleTop)"/>
      <text class="funnel-text on-pale" x="389" y="922" font-size="36" text-anchor="middle">MOVE IN</text>
    </g>
    <g class="tier tier-wife">
      <path d="M322,978 L332,1050 A57,12 0 0 0 445,1050 L455,978 Z" fill="url(#deepBody)"/>
      <ellipse cx="388" cy="978" rx="67" ry="15" fill="url(#deepTop)"/>
      <text class="funnel-text on-deep" x="389" y="1032" font-size="36" text-anchor="middle">WIFE</text>
    </g>
  </g>

  <!-- slide note -->
  <g class="slide-note" text-anchor="end">
    <text class="note-text" transform="translate(1143,318) rotate(-90)">SLIDE 1</text>
    <text class="note-text" transform="translate(1194,318) rotate(-90)">SAMPLE OF MY STYLE.</text>
    <text class="note-text" transform="translate(1246,318) rotate(-90)">LET ME KNOW IF YOU LIKE IT.</text>
    <text class="note-text" transform="translate(1297,318) rotate(-90)">ANY FEEDBACK IS IMPORTANT.</text>
  </g>
</svg>
</body>
</html>
```